Banner 170x60 for Barrel Sauna Rental Banner

Attention, please do every side graphic distance 5cm . It is for attachment.
search for a graphic design in dimension 170x60cm.
we have a barrel sauna rental service and need a banner for the two sides.
please look photos.
big text is: (I CAN RENT ME!!! )in english like: you can rent me
frohe-kistenwelt.de
015293417720
info@frohe-kistenwelt.de
we need an eye catcher design!!!!
Design:
maybe wood in at background.
maybe burning fire and sauna style.
Please don't use my barrell sauna pictures. It is only an example for you what we do. The barrel sauna is on build at the moment.

```html
<!DOCTYPE html>
<html lang="de">
<head>
<meta charset="utf-8">
<title>frohe-kistenwelt.de – Banner</title>
<link rel="stylesheet" href="https://fonts.googleapis.com/css2?family=Montserrat:wght@700;800&family=Bebas+Neue&display=swap">
<style>
  :root {
    --page: #e6e7e9;
    --banner: #000000;
    --white: #ffffff;
    --ink: #000000;
    --flame-deep: #7a2400;
    --flame-mid: #e8610c;
    --flame-hot: #ffb21c;
    --flame-red: #e3200f;
  }
  * { margin: 0; padding: 0; box-sizing: border-box; }
  html, body { width: 1200px; height: 609px; overflow: hidden; background: var(--page); }
  .canvas { position: relative; width: 1200px; height: 609px; }
  .banner {
    position: absolute; left: 85px; top: 123px; width: 1030px; height: 363px;
    background: var(--banner); overflow: hidden;
  }
  .flames-smoke {
    position: absolute; left: 8px; top: 96px; width: 345px; height: 267px;
    background: radial-gradient(ellipse at 50% 100%, var(--flame-hot) 0%, var(--flame-mid) 35%, var(--flame-deep) 62%, rgba(0,0,0,0) 78%);
  }
  .flames-strip {
    position: absolute; left: 348px; top: 282px; width: 682px; height: 81px;
    background: linear-gradient(to top, var(--flame-hot) 0%, var(--flame-mid) 35%, var(--flame-red) 65%, rgba(0,0,0,0) 100%);
  }
  .brand {
    position: absolute; left: 64px; top: 165px; width: 262px; text-align: center;
    color: var(--white); font-family: "Montserrat", sans-serif;
  }
  .brand-name { font-weight: 800; font-size: 26px; letter-spacing: 0.2px; }
  .brand-tagline { font-weight: 700; font-size: 9.5px; margin-top: 6px; letter-spacing: 0.3px; }
  .headline {
    position: absolute; left: 348px; top: 62px; width: 592px;
    color: var(--white); font-family: "Montserrat", sans-serif; font-weight: 800;
    text-align: center; line-height: 1;
  }
  .headline-main { font-size: 97px; letter-spacing: -1px; white-space: nowrap; }
  .headline-sub { font-size: 62px; margin-top: 8px; white-space: nowrap; letter-spacing: -0.5px; }
  .phone {
    position: absolute; left: 458px; top: 232px; display: flex; align-items: center; gap: 4px;
    color: var(--white); font-family: "Montserrat", sans-serif; font-weight: 800; font-size: 42px;
  }
  .phone svg { width: 46px; height: 46px; }
  .contact-pill {
    position: absolute; top: 298px; height: 26px; border-radius: 13px;
    background: var(--white); color: var(--ink); display: flex; align-items: center; gap: 10px;
    padding: 0 10px 0 3px; font-family: "Bebas Neue", sans-serif; font-size: 24px; line-height: 1;
    letter-spacing: 0.6px;
  }
  .contact-pill svg { width: 22px; height: 22px; }
  .contact-email { left: 355px; width: 293px; }
  .contact-web { left: 669px; width: 227px; }
</style>
</head>
<body>
<div class="canvas">
  <section class="banner">
    <div class="flames-smoke" role="img" aria-label="Photographic orange flames rising from the bottom left"></div>
    <div class="flames-strip" role="img" aria-label="Stylised red and orange flames along the bottom edge"></div>

    <div class="brand">
      <div class="brand-name">frohe-kistenwelt.de</div>
      <div class="brand-tagline">MOBILE FASSSAUNA VERMIETUNG</div>
    </div>

    <h1 class="headline">
      <div class="headline-main">SIE KÖNNEN</div>
      <div class="headline-sub">MICH ENGAGIEREN</div>
    </h1>

    <div class="phone">
      <svg viewBox="0 0 48 48" aria-hidden="true">
        <circle cx="24" cy="24" r="21.5" fill="none" stroke="#fff" stroke-width="3"/>
        <path d="M17 13c1.5-1 3-.8 3.6.6l2 4.2c.5 1-.1 2-1 2.6l-1.3.9c1 3.3 3.2 6.2 6 8l1.2-1c.9-.7 2-.9 2.8-.2l3.6 2.8c1.1.8 1 2.3 0 3.4-1.5 1.7-3.8 2.2-6 1.2C21 33 15.6 26 14.5 19.6c-.4-2.6.8-5.3 2.5-6.6z" fill="none" stroke="#fff" stroke-width="2.4" stroke-linejoin="round"/>
      </svg>
      <span>015293417720</span>
    </div>

    <div class="contact-pill contact-email">
      <svg viewBox="0 0 24 24" aria-hidden="true">
        <circle cx="12" cy="12" r="10.5" fill="none" stroke="#000" stroke-width="1.6"/>
        <rect x="6" y="8" width="12" height="8" fill="none" stroke="#000" stroke-width="1.4"/>
        <path d="M6 8l6 4.5L18 8" fill="none" stroke="#000" stroke-width="1.4"/>
      </svg>
      <span>INFO@FROHE-KISTENWELT.DE</span>
    </div>

    <div class="contact-pill contact-web">
      <svg viewBox="0 0 24 24" aria-hidden="true">
        <circle cx="12" cy="12" r="10.5" fill="none" stroke="#000" stroke-width="1.6"/>
        <circle cx="12" cy="12" r="6.5" fill="none" stroke="#000" stroke-width="1.2"/>
        <ellipse cx="12" cy="12" rx="3" ry="6.5" fill="none" stroke="#000" stroke-width="1.2"/>
        <path d="M5.5 12h13M6.5 9h11M6.5 15h11" stroke="#000" stroke-width="1"/>
      </svg>
      <span>FROHE-KISTENWELT.DE</span>
    </div>
  </section>
</div>
</body>
</html>
```